IT solutions & services company requires stationary makeover

Looking for a consistent modern, professional design across our printed client touch points:
Business Cards
Letterhead
Client proposal
Flyer
Postcard

We provide solutions for SME IT - servers, backups, AV etc, and the ongoing services around them.
we are happy with our logo - please see attached and would like the colour theme to be maintained.

```html
<!DOCTYPE html>
<html lang="en">
<head>
<meta charset="utf-8">
<title>Norvax business card</title>
<link href="https://fonts.googleapis.com/css2?family=Questrial&family=Montserrat:wght@700&display=swap" rel="stylesheet">
<style>
  :root{
    --bg:#e9e9ec;
    --card-dark:#262626;
    --card-light:#f6f7f9;
    --ink:#2a2a2a;
    --ink-soft:#4a4a4a;
    --brand-blue:#1a93d1;
    --band-start:#0f6a92;
    --band-end:#1a9ad6;
    --strip:#d9dbdf;
    --white:#ffffff;
  }
  *{box-sizing:border-box;margin:0;padding:0}
  html,body{width:1200px;height:934px;overflow:hidden}
  body{background:var(--bg);font-family:"Questrial",sans-serif;position:relative}

  .card{position:absolute;width:520px;height:300px;overflow:hidden;box-shadow:0 6px 18px rgba(0,0,0,.12)}
  .card--back{left:70px;top:190px;background:var(--card-dark)}
  .card--front{left:610px;top:430px;background:var(--card-light)}

  .brand{display:flex;align-items:center;gap:14px}
  .brand__dot{width:38px;height:38px;border-radius:50%;background:var(--brand-blue);flex:none}
  .brand__text{display:flex;flex-direction:column}
  .brand__name{font-family:"Questrial",sans-serif;font-size:48px;line-height:1;letter-spacing:1px}
  .brand__tagline{font-size:10.5px;letter-spacing:1.2px;margin-top:4px;margin-left:4px;white-space:nowrap}

  .card--back .brand{position:absolute;left:220px;top:112px}
  .card--back .brand__name,.card--back .brand__tagline{color:var(--white)}

  .card--front .brand{position:absolute;left:36px;top:112px}
  .card--front .brand__name{color:var(--ink)}
  .card--front .brand__tagline{color:var(--ink-soft)}

  .person{position:absolute;right:38px;top:40px;text-align:right;color:var(--ink)}
  .person__name{font-family:"Montserrat",sans-serif;font-weight:700;font-size:17px;letter-spacing:.6px}
  .person__role{font-size:13.5px;margin-top:3px;color:var(--ink-soft)}

  .strip{position:absolute;left:0;right:0;top:200px;height:12px;background:var(--strip)}
  .contact-band{position:absolute;left:0;right:0;bottom:0;height:88px;
    background:linear-gradient(90deg,var(--band-start),var(--band-end));
    display:flex;align-items:center;padding:0 22px;color:var(--white);font-size:12.5px}
  .contact-band__col{line-height:1.7;white-space:nowrap}
  .contact-band__col--address{width:178px}
  .contact-band__divider{width:1px;height:34px;background:rgba(255,255,255,.6);margin:0 18px}
  .contact-line{display:flex;align-items:center;gap:7px}
  .contact-line svg{width:12px;height:12px;flex:none}
</style>
</head>
<body>

<section class="card card--back" aria-label="Business card back">
  <div class="brand">
    <span class="brand__dot"></span>
    <div class="brand__text">
      <span class="brand__name">norvax</span>
      <span class="brand__tagline">SYSTEMS THAT KEEP GOING</span>
    </div>
  </div>
</section>

<section class="card card--front" aria-label="Business card front">
  <div class="brand">
    <span class="brand__dot"></span>
    <div class="brand__text">
      <span class="brand__name">norvax</span>
      <span class="brand__tagline">SYSTEMS THAT KEEP GOING</span>
    </div>
  </div>

  <div class="person">
    <p class="person__name">JORDAN PELL</p>
    <p class="person__role">General Director</p>
  </div>

  <div class="strip"></div>

  <div class="contact-band">
    <div class="contact-band__col contact-band__col--address">
      <p>Unit 7 Harrow Trade Park</p>
      <p>Millbank Lane, London</p>
    </div>
    <span class="contact-band__divider"></span>
    <div class="contact-band__col">
      <p class="contact-line">
        <svg viewBox="0 0 12 12" aria-hidden="true"><circle cx="6" cy="6" r="5.3" fill="none" stroke="#fff" stroke-width="1"/><path d="M4 3.2l1 1.4-.6.7c.4.8 1 1.4 1.8 1.8l.7-.6 1.4 1-.6 1C6 8.3 3.7 6 3.4 4z" fill="#fff"/></svg>
        0700-555-010
      </p>
      <p class="contact-line">
        <svg viewBox="0 0 12 12" aria-hidden="true"><circle cx="6" cy="6" r="5.3" fill="none" stroke="#fff" stroke-width="1"/><rect x="3.2" y="5" width="5.6" height="3.4" fill="#fff"/><rect x="4.2" y="3.2" width="3.6" height="1.6" fill="none" stroke="#fff" stroke-width=".8"/></svg>
        0700 555 011
      </p>
    </div>
    <span class="contact-band__divider"></span>
    <div class="contact-band__col">
      <p class="contact-line">
        <svg viewBox="0 0 12 12" aria-hidden="true"><circle cx="6" cy="6" r="5.3" fill="none" stroke="#fff" stroke-width="1"/><rect x="3" y="4" width="6" height="4" fill="none" stroke="#fff" stroke-width=".8"/><path d="M3 4l3 2.3L9 4" fill="none" stroke="#fff" stroke-width=".8"/></svg>
        info@norvaxit.com
      </p>
      <p class="contact-line">
        <svg viewBox="0 0 12 12" aria-hidden="true"><circle cx="6" cy="6" r="5.3" fill="none" stroke="#fff" stroke-width="1"/><ellipse cx="6" cy="6" rx="2.2" ry="5.3" fill="none" stroke="#fff" stroke-width=".8"/><path d="M.8 6h10.4" stroke="#fff" stroke-width=".8"/></svg>
        www.norvaxit.com
      </p>
    </div>
  </div>
</section>

</body>
</html>
```